Car Loan Landing Page Redesign

We are looking for a fresh, eye catching and professional redesign of our landing page as attached.
This current template doesn't stand out and doesn't highlight the main part of the page which is the application box.
Our corporate colors are pink #ee245f, black #000, #232323 and colors as in our website www.brindlecove.com.au
Brindle is Australia's leading car finance brokerage institution and this landing page is geared towards car finance.
We also believe the background banner needs some sort of creative approach.
We also feel that the form steps (once you click on start to compare) needs to be refreshed as well in terms of its form input fields design.
We like to have this whole page redesigned and freshen up so it gives an unique design experience to the users.
Feel free to use your imagination with some great eye catchy banner, and move the elements around as you need to.
Target Market(s)
Australians who are looking for car finance
Industry/Entity Type
Finance
Number of Pages Required
1 page
Font styles to use
Other font styles liked:
- Roboto
Look and feel

```html
<!DOCTYPE html>
<html lang="en">
<head>
<meta charset="utf-8">
<title>Brindle Car Finance</title>
<link rel="stylesheet" href="https://fonts.googleapis.com/css2?family=Roboto:ital,wght@0,300;0,400;0,500;0,700;1,300;1,400&display=swap">
<style>
:root{
  --pink:#ee245f;
  --black:#000;
  --ink:#232323;
  --text:#555;
  --muted:#888;
  --grey:#f2f2f2;
  --box:#e4e4e4;
  --line:#d9d9d9;
  --white:#fff;
}
*{box-sizing:border-box;margin:0;padding:0}
html,body{width:1200px;height:2903px;overflow:hidden}
body{position:relative;font-family:'Roboto',sans-serif;color:var(--ink);background:var(--white)}
.abs{position:absolute}
.btn{position:absolute;background:var(--pink);color:var(--white);font-weight:500;text-transform:uppercase;text-align:center;font-size:11px;letter-spacing:.5px}

/* header */
.site-header{position:absolute;left:0;top:0;width:1200px;height:93px;border-top:4px solid var(--pink);background:var(--white)}
.brand{position:absolute;left:100px;top:14px;width:175px}
.brand-name{font-size:50px;font-weight:400;line-height:50px;color:var(--ink);letter-spacing:-1px}
.brand-sub{font-size:11px;color:var(--ink);letter-spacing:.5px;margin-top:-2px}
.tagline{position:absolute;left:282px;top:50px;font-size:13px;font-style:italic;color:var(--ink)}
.header-apply{left:776px;top:32px;width:118px;height:36px;line-height:36px;font-size:12px}
.call{position:absolute;left:926px;top:28px}
.call svg{position:absolute;left:0;top:4px}
.call-label{position:absolute;left:42px;top:0;font-size:11px;font-weight:700;white-space:nowrap}
.call-number{position:absolute;left:42px;top:14px;font-size:20px;color:#444;white-space:nowrap}

/* hero */
.hero{position:absolute;left:0;top:93px;width:1200px;height:513px;overflow:hidden}
.hero-photo{position:absolute;inset:0;background:linear-gradient(100deg,#7d6a58 0%,#b59a80 25%,#cbb8a2 45%,#8f8676 70%,#3a3a36 100%)}
.hero-arrow{position:absolute;top:227px;width:36px;height:36px;border:2px solid rgba(255,255,255,.8);border-radius:50%}
.hero-title{position:absolute;left:768px;top:206px;font-size:38px;font-weight:300;line-height:44px;color:var(--white)}
.hero-btn{left:766px;top:312px;width:134px;height:36px;line-height:36px}

/* steps */
.section-title{position:absolute;left:0;width:1200px;text-align:center;font-weight:300;color:var(--ink)}
.section-sub{position:absolute;left:0;width:1200px;text-align:center;font-size:15px;color:var(--text)}
.steps-line{position:absolute;left:232px;top:818px;width:748px;height:1px;background:var(--line)}
.step{position:absolute;top:772px;width:220px;margin-left:-110px;text-align:center}
.step-icon{width:92px;height:92px;border-radius:50%;background:#e9e7e2;margin:0 auto;display:flex;align-items:center;justify-content:center}
.step-icon.active{background:var(--pink)}
.step-title{font-size:15px;margin-top:12px}
.step-text{font-size:12px;color:var(--text);line-height:16px;margin-top:8px}

/* borrow slider */
.borrow{position:absolute;left:0;top:1000px;width:1200px;height:273px;overflow:hidden}
.borrow-photo{position:absolute;inset:0;background:linear-gradient(90deg,#1d1d1d 0%,#2d2a27 45%,#4a423b 70%,#3b3530 100%)}
.borrow-title{position:absolute;left:108px;top:36px;font-size:25px;font-weight:300;color:var(--white)}
.borrow-value{position:absolute;left:963px;top:37px;width:118px;height:36px;border:1px solid #ccc;color:var(--white);text-align:center;line-height:34px;font-size:18px}
.track{position:absolute;left:108px;top:130px;width:976px;height:5px;background:#6a6a6a;border-radius:3px}
.track-fill{position:absolute;left:0;top:0;width:46px;height:5px;background:var(--pink);border-radius:3px}
.tick{position:absolute;top:-3px;width:1px;height:11px;background:#9a9a9a}
.bubble{position:absolute;left:112px;top:100px;width:38px;height:20px;border:1px solid #aaa;color:var(--white);font-size:11px;text-align:center;line-height:18px}
.scale{position:absolute;left:108px;top:150px;width:976px;display:flex;justify-content:space-between;color:var(--white);font-size:12px}
.compare-btn{left:519px;top:205px;width:162px;height:36px;line-height:36px}

/* lenders */
.lenders{position:absolute;left:99px;top:1442px;display:flex;gap:14px}
.lender{width:162px;height:62px;border:1px solid var(--line);display:flex;align-items:center;justify-content:center;gap:8px;font-size:19px;font-weight:500;color:var(--ink)}
.lender-dot{width:14px;height:14px;border-radius:50%;background:var(--ink)}

/* features */
.features{position:absolute;left:0;top:1567px;width:1200px;height:445px;background:var(--grey)}
.feature{position:absolute;width:305px;height:152px;background:linear-gradient(105deg,var(--box) 0%,var(--box) 86%,#ececec 86%,#ececec 100%);text-align:center;padding-top:18px}
.feature svg{display:block;margin:0 auto}
.feature-title{color:var(--pink);font-size:14px;margin-top:8px;text-transform:uppercase}
.feature-text{font-size:11.5px;color:var(--text);line-height:17px;margin:6px auto 0;width:250px}

/* how */
.how-item{position:absolute;width:320px}
.how-icon{position:absolute;left:0;top:0;width:56px;height:56px;border-radius:50%;background:var(--pink);display:flex;align-items:center;justify-content:center}
.how-text{position:absolute;left:74px;top:0;width:250px;font-size:12px;line-height:17px;color:var(--text)}
.road-photo{position:absolute;left:0;top:2340px;width:1200px;height:439px;background:linear-gradient(180deg,#ffffff 0%,#e3e6ea 25%,#9aa2aa 55%,#4d5257 80%,#3a3d40 100%)}
.cta{position:absolute;left:99px;top:2622px;width:1002px;height:92px;background:var(--black);outline:1px dashed #777;outline-offset:-6px}
.cta-text{position:absolute;left:40px;top:14px;font-size:27px;font-style:italic;font-weight:300;color:var(--white);line-height:32px}
.cta-btn{left:794px;top:30px;width:168px;height:33px;line-height:33px}

/* footer */
.site-footer{position:absolute;left:0;top:2779px;width:1200px;height:124px;background:#e9e9e9}
.social{position:absolute;left:104px;top:26px;display:flex;gap:9px}
.social span{width:24px;height:24px;border-radius:50%;background:#3b5998}
.copyright{position:absolute;left:104px;top:80px;font-size:12px;color:var(--ink)}
.badge{position:absolute;top:30px;width:158px;height:68px;background:var(--white);border:1px solid var(--line);display:flex;align-items:center;justify-content:center}
</style>
</head>
<body>

<header class="site-header">
  <div class="brand">
    <div class="brand-name">Brindle</div>
    <div class="brand-sub">finance + insurance</div>
  </div>
  <div class="tagline">Brindle Has Helped Over 35,000 Australians With Their Finance!</div>
  <div class="btn header-apply">Apply Now</div>
  <div class="call">
    <svg width="32" height="32" viewBox="0 0 32 32"><circle cx="16" cy="16" r="15" fill="none" stroke="#232323" stroke-width="2"/><path d="M11 9l3 0 1.5 4-2 1.5c1 2 2.5 3.5 4.5 4.5l1.5-2 4 1.5v3c0 1-1 2-2 2-7 0-12.5-5.5-12.5-12.5 0-1 1-2 2-2z" fill="#232323"/></svg>
    <div class="call-label">CALL US NOW!</div>
    <div class="call-number">(1300) 555 018</div>
  </div>
</header>

<section class="hero">
  <div class="hero-photo" role="img" aria-label="Smiling family sitting in the front seats of a car"></div>
  <div class="hero-arrow" style="left:30px"><svg width="32" height="32" viewBox="0 0 32 32"><path d="M19 9l-7 7 7 7" fill="none" stroke="#fff" stroke-width="2"/></svg></div>
  <div class="hero-arrow" style="left:1132px"><svg width="32" height="32" viewBox="0 0 32 32"><path d="M13 9l7 7-7 7" fill="none" stroke="#fff" stroke-width="2"/></svg></div>
  <h1 class="hero-title">Drive Your Car With<br>A Better Deal!</h1>
  <div class="btn hero-btn">Car Finance</div>
</section>

<h2 class="section-title" style="top:678px;font-size:32px">How Much Can You Save On Your Car Loan?</h2>
<p class="section-sub" style="top:724px">Comparing car loan lenders Could save you Thousands!</p>
<div class="steps-line"></div>
<div class="step" style="left:344px">
  <div class="step-icon active"><svg width="28" height="34" viewBox="0 0 28 34"><path d="M2 2h16l8 8v22H2z M18 2v8h8" fill="none" stroke="#fff" stroke-width="2"/><path d="M8 17h12M8 22h12M8 27h8" stroke="#fff" stroke-width="2"/></svg></div>
  <div class="step-title">Step 1</div>
  <div class="step-text">Tell us how much you need<br>for your next car.</div>
</div>
<div class="step" style="left:608px">
  <div class="step-icon"><span style="font-size:34px;color:#232323">%</span></div>
  <div class="step-title">Step 2</div>
  <div class="step-text">We provide lightning quick<br>quotes from our lenders.</div>
</div>
<div class="step" style="left:867px">
  <div class="step-icon"><svg width="52" height="26" viewBox="0 0 52 26"><path d="M3 18v-6l6-2 7-7h18l8 7 7 2v6z" fill="none" stroke="#232323" stroke-width="2"/><circle cx="14" cy="19" r="4" fill="#e9e7e2" stroke="#232323" stroke-width="2"/><circle cx="39" cy="19" r="4" fill="#e9e7e2" stroke="#232323" stroke-width="2"/></svg></div>
  <div class="step-title">Step 3</div>
  <div class="step-text">Gain approval and drive away<br>with a better deal!</div>
</div>

<section class="borrow">
  <div class="borrow-photo" role="img" aria-label="Young couple holding a cardboard house roof over their heads"></div>
  <h2 class="borrow-title">How Much Do You Like To Borrow?</h2>
  <div class="borrow-value">$5,000</div>
  <div class="bubble">$5K</div>
  <div class="track">
    <div class="track-fill"></div>
    <i class="tick" style="left:0"></i><i class="tick" style="left:81px"></i><i class="tick" style="left:162px"></i><i class="tick" style="left:244px"></i><i class="tick" style="left:325px"></i><i class="tick" style="left:406px"></i><i class="tick" style="left:488px"></i><i class="tick" style="left:569px"></i><i class="tick" style="left:650px"></i><i class="tick" style="left:732px"></i><i class="tick" style="left:813px"></i><i class="tick" style="left:894px"></i><i class="tick" style="left:975px"></i>
  </div>
  <div class="scale"><span>$5K</span><span>$15K</span><span>$24K</span><span>$34K</span><span>$43K</span><span>$53K</span><span>$63K</span><span>$72K</span><span>$82K</span><span>$91K</span><span>$101K</span><span>$110K</span><span>$120K</span></div>
  <div class="btn compare-btn">Start To Compare</div>
</section>

<h2 class="section-title" style="top:1345px;font-size:30px">Compare Multiple lenders &amp; Save on your finance.Get Brindle</h2>
<p class="section-sub" style="top:1392px;font-size:12px">Comparing lenders can help you get great rates and save thousands! Compare Australia's top lenders with Brindle and save.</p>
<div class="lenders">
  <div class="lender">Fundra</div>
  <div class="lender">Harbourline</div>
  <div class="lender">Saltbush</div>
  <div class="lender"><span class="lender-dot"></span>Keelwater</div>
  <div class="lender" style="width:100px;font-size:16px">Tallow</div>
  <div class="lender" style="width:150px">Ridgebank</div>
</div>

<section class="features">
  <div class="feature" style="left:99px;top:55px">
    <svg width="70" height="40" viewBox="0 0 70 40"><circle cx="35" cy="12" r="8" fill="none" stroke="#ee245f" stroke-width="2"/><path d="M20 38c0-10 7-16 15-16s15 6 15 16z" fill="none" stroke="#ee245f" stroke-width="2"/><circle cx="18" cy="16" r="6" fill="none" stroke="#ee245f" stroke-width="2"/><circle cx="52" cy="16" r="6" fill="none" stroke="#ee245f" stroke-width="2"/></svg>
    <div class="feature-title">Reputable Lenders</div>
    <div class="feature-text">Brindle is an accredited NFBA member and represents 25+ repu..[+]</div>
  </div>
  <div class="feature" style="left:447px;top:55px">
    <svg width="70" height="40" viewBox="0 0 70 40"><rect x="14" y="8" width="42" height="22" fill="none" stroke="#232323" stroke-width="2"/><rect x="18" y="13" width="42" height="22" fill="#e4e4e4" stroke="#232323" stroke-width="2"/><circle cx="39" cy="24" r="5" fill="none" stroke="#232323" stroke-width="2"/></svg>
    <div class="feature-title">Compare &amp; Save</div>
    <div class="feature-text">Compare and save with Brindle. Brindle will shop your deal around ..[+]</div>
  </div>
  <div class="feature" style="left:795px;top:55px">
    <svg width="70" height="40" viewBox="0 0 70 40"><circle cx="27" cy="9" r="6" fill="none" stroke="#232323" stroke-width="2"/><circle cx="43" cy="31" r="6" fill="none" stroke="#ee245f" stroke-width="2"/><path d="M47 4L23 36" stroke="#232323" stroke-width="2"/></svg>
    <div class="feature-title">Low Interest Rates</div>
    <div class="feature-text">Brindle, through its lending panel can provide youwith some ..[+]</div>
  </div>
  <div class="feature" style="left:99px;top:242px">
    <svg width="70" height="44" viewBox="0 0 70 44"><circle cx="35" cy="22" r="19" fill="none" stroke="#232323" stroke-width="2"/><path d="M35 10v13" stroke="#ee245f" stroke-width="2"/></svg>
    <div class="feature-title">Same Day Approvals</div>
    <div class="feature-text">Our application process is quick &amp; easy. Brindle has the systems..[+]</div>
  </div>
  <div class="feature" style="left:447px;top:242px">
    <svg width="70" height="44" viewBox="0 0 70 44"><path d="M30 4h10l-3 7h-4z" fill="none" stroke="#232323" stroke-width="2"/><path d="M33 11c-10 6-14 14-14 21 0 6 5 9 16 9s16-3 16-9c0-7-4-15-14-21z" fill="none" stroke="#232323" stroke-width="2"/><text x="35" y="34" font-size="14" text-anchor="middle" fill="#ee245f" font-family="Roboto,sans-serif">$</text></svg>
    <div class="feature-title">100% Finance</div>
    <div class="feature-text">100% finance is available to approved customersas the car..[+]</div>
  </div>
  <div class="feature" style="left:795px;top:242px">
    <svg width="70" height="44" viewBox="0 0 70 44"><circle cx="35" cy="22" r="19" fill="none" stroke="#232323" stroke-width="2"/><path d="M26 22l7 7 14-15" fill="none" stroke="#ee245f" stroke-width="2.5"/></svg>
    <div class="feature-title">No Obligation</div>
    <div class="feature-text">All applications with Brindle are obligation free...[+]</div>
  </div>
</section>

<h2 class="section-title" style="top:2107px;font-size:27px">How Brindle Will Help You Find A Great Deal&nbsp; On Your Car Finance</h2>
<div class="road-photo" role="img" aria-label="Black sports car driving on an open road under a bright sky"></div>

<div class="how-item" style="left:103px;top:2186px">
  <div class="how-icon"><svg width="26" height="26" viewBox="0 0 26 26"><path d="M3 12L23 3l-9 20-2-9z" fill="none" stroke="#fff" stroke-width="2"/></svg></div>
  <div class="how-text">Understand Your Needs And Requirements And Find A Tailored Loan Solution Based On Your Financial Goals.</div>
</div>
<div class="how-item" style="left:447px;top:2186px">
  <div class="how-icon"><svg width="22" height="28" viewBox="0 0 22 28"><path d="M11 26C5 18 2 14 2 10a9 9 0 0118 0c0 4-3 8-9 16z" fill="none" stroke="#fff" stroke-width="2"/><circle cx="11" cy="10" r="3" fill="#fff"/></svg></div>
  <div class="how-text">Ascertain your borrowing power, your capacity for repayments so you always get a loan thats within your budget.</div>
</div>
<div class="how-item" style="left:790px;top:2186px">
  <div class="how-icon"><svg width="22" height="26" viewBox="0 0 22 26"><rect x="2" y="2" width="18" height="22" fill="none" stroke="#fff" stroke-width="2"/><circle cx="11" cy="11" r="3" fill="none" stroke="#fff" stroke-width="2"/><path d="M6 20c1-3 3-4 5-4s4 1 5 4" fill="none" stroke="#fff" stroke-width="2"/></svg></div>
  <div class="how-text">Compare your car loan with 25+ lenders andbanks so you gain the best deal from a top leader.</div>
</div>
<div class="how-item" style="left:103px;top:2284px">
  <div class="how-icon"><svg width="28" height="28" viewBox="0 0 28 28"><circle cx="14" cy="14" r="11" fill="none" stroke="#fff" stroke-width="2"/><text x="14" y="19" font-size="13" text-anchor="middle" fill="#fff" font-family="Roboto,sans-serif">$</text></svg></div>
  <div class="how-text">Provide you with a dedicated personal consultant to manage your application and delivery - every step of the way.</div>
</div>
<div class="how-item" style="left:447px;top:2284px">
  <div class="how-icon"><svg width="30" height="18" viewBox="0 0 30 18"><path d="M2 12V8l4-1 4-5h10l5 5 3 1v4z" fill="none" stroke="#fff" stroke-width="2"/><circle cx="8" cy="13" r="2.5" fill="#ee245f" stroke="#fff" stroke-width="2"/><circle cx="22" cy="13" r="2.5" fill="#ee245f" stroke="#fff" stroke-width="2"/></svg></div>
  <div class="how-text">Explain all fees charges and obligations up front so you know exactly what youre getting when it come to your car loan.</div>
</div>
<div class="how-item" style="left:790px;top:2284px">
  <div class="how-icon"><svg width="26" height="26" viewBox="0 0 26 26"><path d="M5 13l6 6 11-13" fill="none" stroke="#fff" stroke-width="2.5"/></svg></div>
  <div class="how-text">Provide you with highest level of customer services and support throghout the life of your loan.</div>
</div>

<div class="cta">
  <div class="cta-text">Compare Australia's Top Lenders With Us<br>Today. Get Brindle!</div>
  <div class="btn cta-btn">Compare Car Loans</div>
</div>

<footer class="site-footer">
  <div class="social">
    <span style="background:#3b5998"></span><span style="background:#2aa9e0"></span><span style="background:#0e76a8"></span><span style="background:#dd4b39"></span><span style="background:#cb2027"></span><span style="background:#6d84b4"></span>
  </div>
  <div class="copyright">© 2016 Brindlecarloans. All Rights Reserved</div>
  <div class="badge" style="left:600px"><span style="width:26px;height:40px;background:#e8c21e;display:block"></span></div>
  <div class="badge" style="left:770px"><span style="width:90px;height:30px;border-radius:50%;background:#8ea3b5;display:block"></span></div>
  <div class="badge" style="left:940px"><span style="width:40px;height:40px;border-radius:50%;background:#3f7d4a;display:block"></span></div>
</footer>

</body>
</html>
```